Delmer's Pressure Washing Services

Starting a pressure washing business on my own in Central Valley California, not too much experience so affordable, I do houses, fences, driveways, cars, trailers, RVs. Planning to make this full-time hoping clientele picks up after having a nice business card. Design doesn't have to be flashy, more to the point, I like simplistic/personable. I do not want something exhausting to look at or with too much going on.

Target Market(s)

Residential, Commercial

Industry/Entity Type

Pressure Washing

Contact Information for Business Card

avalible Services

Font styles to use
Sans Serif

Colors
0054AA
0677BA
7BADD7
CADEEF
E8F1F8
0094D4
00A9DD
6FCCEA
C7EBF8
E9F6FB
00AB8E
00BBA5
67D7C9
C6EFE9
E9F9F6

```html
<!DOCTYPE html>
<html lang="en">
<head>
<meta charset="UTF-8">
<title>Delmer's Pressure Washing Services – Business Card</title>
<link href="https://fonts.googleapis.com/css2?family=Open+Sans:ital,wght@0,400;0,600;1,800&family=Roboto+Condensed:wght@700&display=swap" rel="stylesheet">
<style>
  :root {
    --page: #ffffff;
    --card-light: #e4f2fa;
    --card-pale: #eef7fc;
    --sky: #93d3ef;
    --cyan: #5fc3e6;
    --cyan-deep: #1fb8e0;
    --band: #0aa8dc;
    --brand-blue: #0677ba;
    --line-blue: #1a9ad6;
    --ink: #1b2733;
    --white: #ffffff;
  }
  * { margin: 0; padding: 0; box-sizing: border-box; }
  html, body {
    width: 1200px; height: 1001px; overflow: hidden;
    background: var(--page);
    font-family: "Open Sans", sans-serif;
  }
  .card {
    position: absolute; left: 294px;
    width: 612px; height: 350px; overflow: hidden;
  }
  .card--front { top: 73px; background: linear-gradient(90deg, var(--card-pale), var(--card-light)); }
  .card--back {
    top: 536px;
    background:
      radial-gradient(ellipse 60% 70% at 100% 85%, var(--cyan-deep) 0%, rgba(95,195,230,0.6) 45%, rgba(95,195,230,0) 80%),
      radial-gradient(ellipse 40% 50% at 95% 15%, rgba(95,195,230,0.7), rgba(95,195,230,0) 80%),
      linear-gradient(180deg, var(--sky) 0%, #c4e5f5 60%, #e3f2fb 100%);
  }
  .front-panel { position: absolute; inset: 0; }
  .title {
    position: absolute; left: 36px; top: 110px;
    font-weight: 800; font-style: italic; font-size: 64px; line-height: 58px;
    color: var(--white);
    -webkit-text-stroke: 4px var(--line-blue);
    paint-order: stroke fill;
    letter-spacing: 1px;
    white-space: nowrap;
  }
  .title span { display: block; }
  .title .line-2 { padding-left: 14px; }
  .contact {
    position: absolute; right: 23px; top: 120px; width: 170px;
    text-align: right; color: var(--brand-blue);
  }
  .contact .phone {
    font-family: "Roboto Condensed", sans-serif; font-weight: 700;
    font-size: 31px; line-height: 36px; color: var(--brand-blue);
    white-space: nowrap;
  }
  .contact .owner { font-size: 15px; line-height: 20px; margin-top: 2px; }
  .contact .rule { height: 1.5px; background: var(--brand-blue); margin: 12px 0 14px auto; width: 146px; }
  .contact .area { font-size: 15px; line-height: 21px; }
  .band { position: absolute; height: 20px; background: var(--band); }
  .band--top { left: 0; top: 53px; width: 289px; border-radius: 0 10px 10px 0; }
  .band--bottom { left: 323px; top: 276px; width: 289px; border-radius: 10px 0 0 10px; }
  .services { position: absolute; left: 0; top: 128px; width: 612px; }
  .service {
    position: absolute; width: 100px; margin-left: -50px;
    text-align: center;
  }
  .service svg { display: block; margin: 0 auto; }
  .service .label { margin-top: 10px; font-size: 16px; line-height: 20px; color: var(--ink); white-space: nowrap; }
</style>
</head>
<body>

<section class="card card--front">
  <svg class="front-panel" width="612" height="350" viewBox="0 0 612 350" role="img" aria-label="Blue panel scattered with water droplets">
    <defs>
      <radialGradient id="panelFill" cx="0.75" cy="0.7" r="0.8">
        <stop offset="0" stop-color="#5fc3e6"/>
        <stop offset="0.45" stop-color="#cfe9f6"/>
        <stop offset="0.75" stop-color="#a8dbf1"/>
        <stop offset="1" stop-color="#93d3ef"/>
      </radialGradient>
    </defs>
    <path d="M0 0 H312 A198 198 0 0 1 312 350 H0 Z" fill="url(#panelFill)"/>
  </svg>
  <h1 class="title"><span class="line-1">PRESSURE</span><span class="line-2">WASHING</span></h1>
  <div class="contact">
    <div class="phone">2095550148</div>
    <div class="owner">DELMER ORTIZ</div>
    <div class="rule"></div>
    <div class="area">IN CENTRAL<br>VALLEY CALIFORNIA</div>
  </div>
</section>

<section class="card card--back" role="img" aria-label="Blue gradient with water droplets">
  <div class="band band--top"></div>
  <div class="band band--bottom"></div>
  <div class="services">
    <div class="service" style="left:71px">
      <svg width="62" height="62" viewBox="0 0 62 62" fill="none" stroke="#1b2733" stroke-width="1.4">
        <circle cx="31" cy="31" r="30" stroke="#1a9ad6" stroke-width="1.6"/>
        <path d="M17 31 L31 18 L45 31"/><path d="M21 28 V44 H41 V28"/><path d="M28 44 V36 H34 V44"/>
      </svg>
      <div class="label">HOUSES</div>
    </div>
    <div class="service" style="left:165px">
      <svg width="62" height="62" viewBox="0 0 62 62" fill="none" stroke="#1b2733" stroke-width="1.4">
        <circle cx="31" cy="31" r="30" stroke="#1a9ad6" stroke-width="1.6"/>
        <path d="M17 21V43M21 21V43M25 21V43M29 21V43M33 21V43M37 21V43M41 21V43M45 21V43M15 27H47M15 38H47"/>
      </svg>
      <div class="label">FENCES</div>
    </div>
    <div class="service" style="left:259px">
      <svg width="62" height="62" viewBox="0 0 62 62" fill="none" stroke="#1b2733" stroke-width="1.4">
        <circle cx="31" cy="31" r="30" stroke="#1a9ad6" stroke-width="1.6"/>
        <path d="M29 19 L17 43M33 19 L45 43M31 22V26M31 30V35M31 39V44"/>
      </svg>
      <div class="label">DRIVEWAYS</div>
    </div>
    <div class="service" style="left:354px">
      <svg width="62" height="62" viewBox="0 0 62 62" fill="none" stroke="#1b2733" stroke-width="1.4">
        <circle cx="31" cy="31" r="30" stroke="#1a9ad6" stroke-width="1.6"/>
        <path d="M9 36 V32 Q11 29 18 28 L24 24 H36 L43 28 Q52 29 53 33 V36 H47 M15 36 H9 M21 36 H41"/>
        <circle cx="18" cy="36" r="3"/><circle cx="44" cy="36" r="3"/>
      </svg>
      <div class="label">CARS</div>
    </div>
    <div class="service" style="left:448px">
      <svg width="62" height="62" viewBox="0 0 62 62" fill="none" stroke="#1b2733" stroke-width="1.4">
        <circle cx="31" cy="31" r="30" stroke="#1a9ad6" stroke-width="1.6"/>
        <path d="M20 24 H52 V32 H20 Z M11 34 L20 30 M20 33 H52"/>
        <circle cx="27" cy="37" r="3"/><circle cx="45" cy="37" r="3"/>
      </svg>
      <div class="label">TRAILERS</div>
    </div>
    <div class="service" style="left:543px">
      <svg width="62" height="62" viewBox="0 0 62 62" fill="none" stroke="#1b2733" stroke-width="1.4">
        <circle cx="31" cy="31" r="30" stroke="#1a9ad6" stroke-width="1.6"/>
        <path d="M11 22 H44 Q51 26 52 34 V39 H11 Z M28 19 H38 V22"/>
        <rect x="15" y="26" width="10" height="5"/><rect x="29" y="26" width="6" height="11"/><path d="M40 26 H47 L49 31 H40 Z"/>
        <circle cx="19" cy="40" r="3"/><circle cx="44" cy="40" r="3"/>
      </svg>
      <div class="label">RVS</div>
    </div>
  </div>
</section>

</body>
</html>
```